Building company needs a letterhead design

I'm after a modern but professional letter head.
Must have the below details:
- Logo
- Website - TARVELBUILD.COM.AU
- Email - INFO@TARVELBUILD.COM.AU
- Office - 03 52631848
- Mobile number - 0413596281
- ABN - 47 318 965 102
...........................................................................................................................................................................................................................
- Logo
- Office - 03 52631848
- ABN - 47 318 965 102

Target Market(s)

.

Industry/Entity Type

Construction Company

Font styles to use
Sans Serif

Requirements
Must have
• Must have the below details:
• - Logo
• - Website - TARVELBUILD.COM.AU
• - Email - INFO@TARVELBUILD.COM.AU
• - Office - 03 52631848
• - Mobile number - 0413596281
• - ABN - 47 318 965 102
Nice to have
• .
Should not have
• .

```html
<!DOCTYPE html>
<html lang="en">
<head>
<meta charset="utf-8">
<title>Tarvel Building Group Letterhead</title>
<link rel="stylesheet" href="https://fonts.googleapis.com/css2?family=Open+Sans:wght@400;700&display=swap">
<style>
  :root {
    --backdrop: #e6e6e4;
    --paper: #ffffff;
    --brand-yellow: #fbb516;
    --brand-grey: #6d6e71;
    --ink: #4a4a4a;
  }
  html, body {
    margin: 0;
    width: 1186px;
    height: 1200px;
    overflow: hidden;
    background: var(--backdrop);
    font-family: "Open Sans", sans-serif;
  }
  .letterhead {
    position: absolute;
    left: 197px;
    top: 40px;
    width: 792px;
    height: 1120px;
    background: var(--paper);
    box-shadow: 0 4px 14px rgba(0,0,0,0.18);
    overflow: hidden;
  }
  .brand {
    position: absolute;
    top: 78px;
    right: 70px;
    display: flex;
    align-items: center;
    gap: 12px;
  }
  .brand-square {
    width: 44px;
    height: 44px;
    background: var(--brand-yellow);
  }
  .brand-name {
    font-weight: 700;
    font-size: 26px;
    letter-spacing: 1px;
    color: var(--brand-grey);
    line-height: 1;
  }
  .footer-wave {
    position: absolute;
    left: 0;
    top: 0;
    width: 792px;
    height: 1120px;
  }
  .wave-grey { fill: var(--brand-grey); }
  .wave-yellow { fill: var(--brand-yellow); }
  .contact-line {
    position: absolute;
    left: 0;
    right: 0;
    bottom: 12px;
    display: flex;
    justify-content: center;
    align-items: center;
    gap: 14px;
    font-size: 11.5px;
    color: var(--ink);
  }
  .contact-item {
    display: flex;
    align-items: center;
    gap: 5px;
  }
  .contact-item svg {
    width: 11px;
    height: 11px;
    fill: var(--ink);
  }
</style>
</head>
<body>
  <main class="letterhead">
    <div class="brand">
      <span class="brand-square"></span>
      <span class="brand-name">TARVEL BUILDING GROUP</span>
    </div>

    <svg class="footer-wave" viewBox="0 0 792 1120" aria-hidden="true">
      <path class="wave-grey" d="M0 840 C 40 930, 160 985, 380 1010 C 560 1030, 700 1050, 792 1082 L 792 1120 L 0 1120 Z"/>
      <path class="wave-yellow" d="M0 905 C 70 955, 170 990, 380 1020 C 560 1045, 700 1062, 792 1092 L 792 1120 L 0 1120 Z"/>
    </svg>

    <div class="contact-line">
      <span class="contact-item">
        <svg viewBox="0 0 12 12"><path d="M2.5 0.5 L4.5 0.5 L5.3 3 L4 4.2 C4.7 5.6 6.3 7.3 7.8 8 L9 6.7 L11.5 7.5 L11.5 9.5 C11.5 10.6 10.6 11.5 9.5 11.5 C4.7 11.5 0.5 7.3 0.5 2.5 C0.5 1.4 1.4 0.5 2.5 0.5 Z"/></svg>
        03 52631848
      </span>
      <span class="contact-item">
        <svg viewBox="0 0 12 12"><path d="M3 0 H9 A1 1 0 0 1 10 1 V11 A1 1 0 0 1 9 12 H3 A1 1 0 0 1 2 11 V1 A1 1 0 0 1 3 0 Z M3.5 1.5 V9.5 H8.5 V1.5 Z"/></svg>
        0413596281
      </span>
      <span class="contact-item">
        <svg viewBox="0 0 12 12"><path d="M0.5 2 H11.5 V10 H0.5 Z M1.5 3 L6 6.5 L10.5 3 Z"/></svg>
        info@tarvelbuild.com.au
      </span>
      <span class="contact-item">
        <svg viewBox="0 0 12 12"><path d="M6 0.5 A5.5 5.5 0 1 0 6 11.5 A5.5 5.5 0 1 0 6 0.5 Z M6 1.6 C5 2.8 4.6 4.3 4.6 6 C4.6 7.7 5 9.2 6 10.4 C7 9.2 7.4 7.7 7.4 6 C7.4 4.3 7 2.8 6 1.6 Z"/></svg>
        www.tarvelbuild.com.au
      </span>
      <span>|</span>
      <span class="contact-item">ABN: 47 318 965 102</span>
    </div>
  </main>
</body>
</html>
```